Business Card for Language School (2 locations)

We need a sleek business card for a language school that is looking to update our image to be more professional. We work with students ages Pre-Kindergarten through adults. Our idea is to have an all-black business card with white or silver lettering. On the front will be the name of our school (Bright Maple English Academy), and on the back there will be information for our location, phone number, email, and website (and possibly social media information). We have two school branches, so the address, phone number, and email address will be different for each branch, but all of the other information will stay the same. We'd like each branch to have a different color card edge that is neon. We are also open to suggestions and new ideas!

Some answers to questions we have received:
1. The reason we haven't added a logo is because we are looking to get a new one. We hadn't originally planned to do that at this time, but we are going to look into updating our project to include that as another aspect of it. We had previously planned to just include the school name on the front without a logo at this time.
2. We currently have two branches of our school, and we want our business card design to be uniform for each location. While it might make sense to put the information on one card right now, we plan to have more locations in the future, so we want to plan ahead with a unified design right now.
3. Our school addresses and phone numbers can be found on our website: www.brightmapleenglish.example (at the bottom of the page)!
Updates

Part of this contest is also a new logo design. Our previous design was a train, which we would be open to keeping if it had an updated, sleeker design.

Contact Information for Business Card

Card #1:
Bright Maple English Academy (Qiaolin Branch)
Yuqing W. Rd. Sec. 3, Lane 412, No. 29, 1F
Beitou District, Taipei City 11268
02-2649-3058
qiaolin@brightmapleenglish.example

Card #2:
Bright Maple English Academy (Fenghe Branch)
Fulan Road, No. 318, 1F
Songshan District, Taipei City 10573
02-2761-4402
fenghe@brightmapleenglish.example

Both cards:
Website: www.brightmapleenglish.example
Facebook: www.facebook.com/brightmapleenglish
Instagram: @brightmapleenglish

```html
<!DOCTYPE html>
<html lang="en">
<head>
<meta charset="utf-8">
<title>Bright Maple English Academy – Business Card</title>
<link rel="stylesheet" href="https://fonts.googleapis.com/css2?family=Didact+Gothic&family=Urbanist:wght@600;700&display=swap">
<style>
  :root {
    --page-bg: #161616;
    --card-bg: #1e1e1e;
    --card-glow: #3a3a3a;
    --text-white: #ffffff;
    --text-soft: #e6e6e6;
    --text-silver: #bdbdbd;
    --rule: #d9d9d9;
    --mark: #2b2b2b;
  }
  * { margin: 0; padding: 0; box-sizing: border-box; }
  html, body {
    width: 1200px;
    height: 897px;
    overflow: hidden;
    background: var(--page-bg);
  }
  .canvas {
    position: relative;
    width: 1200px;
    height: 897px;
  }
  .card {
    position: absolute;
    left: 303px;
    width: 594px;
    height: 339px;
    background: var(--card-bg);
    color: var(--text-soft);
    text-align: center;
    font-family: "Didact Gothic", "Century Gothic", sans-serif;
  }
  .card--front {
    top: 92px;
    background: radial-gradient(ellipse 60% 55% at 72% 18%, var(--card-glow), var(--card-bg) 70%);
  }
  .card--back { top: 469px; }

  .card__line {
    position: absolute;
    left: 0;
    right: 0;
    white-space: nowrap;
  }
  .school-name {
    top: 24px;
    font-family: "Urbanist", "Century Gothic", sans-serif;
    font-weight: 700;
    font-size: 35px;
    color: var(--text-white);
    letter-spacing: 0.2px;
  }
  .branch-name {
    top: 71px;
    font-family: "Urbanist", "Century Gothic", sans-serif;
    font-weight: 700;
    font-size: 21px;
    color: var(--text-white);
  }
  .divider {
    position: absolute;
    left: 137px;
    width: 320px;
    height: 2px;
    background: linear-gradient(90deg, transparent, var(--rule) 50%, transparent);
  }
  .divider--top { top: 121px; }
  .divider--bottom { top: 263px; }
  .detail { font-size: 18.5px; line-height: 1; }
  .detail--address-1 { top: 141px; }
  .detail--address-2 { top: 164px; }
  .detail--contact { top: 201px; }
  .detail--web { top: 224px; }
  .detail--social { top: 285px; }

  .brand {
    position: absolute;
    top: 104px;
    left: 0;
    right: 0;
    display: flex;
    justify-content: center;
    align-items: center;
    gap: 28px;
  }
  .brand__square {
    width: 112px;
    height: 112px;
    background: var(--mark);
  }
  .brand__name {
    font-family: "Urbanist", "Century Gothic", sans-serif;
    font-weight: 700;
    font-size: 38px;
    line-height: 45px;
    color: var(--text-silver);
    text-align: left;
  }
</style>
</head>
<body>
<main class="canvas">
  <section class="card card--front" aria-label="Card front">
    <h1 class="card__line school-name">Bright Maple English Academy</h1>
    <p class="card__line branch-name">(Qiaolin Branch)</p>
    <div class="divider divider--top"></div>
    <p class="card__line detail detail--address-1">Yuqing W. Rd. Sec. 3, Lane 412, No. 29, 1F</p>
    <p class="card__line detail detail--address-2">Beitou District, Taipei City 11268</p>
    <p class="card__line detail detail--contact">P: 02-2649-3058 &nbsp;|&nbsp; E: qiaolin@brightmapleenglish.example</p>
    <p class="card__line detail detail--web">www.brightmapleenglish.example</p>
    <div class="divider divider--bottom"></div>
    <p class="card__line detail detail--social">Fb: /brightmapleenglish &nbsp;|&nbsp; Ins: @brightmapleenglish</p>
  </section>

  <section class="card card--back" aria-label="Card back">
    <div class="brand">
      <div class="brand__square"></div>
      <p class="brand__name">Bright Maple<br>English<br>Academy</p>
    </div>
  </section>
</main>
</body>
</html>
```